Superfoods Nutrition for Elderly

We need a thematic packaging design that fits our elderly nutrition products, that is based on our "3 Ws ethos" - eating Wisely, Widely & Wholly.

Wisely - selected superfoods and ingredients - NZ and other sources
Widely - based on the "rainbow diet" philosophy
Wholly - all natural, (no artificial flavours, colors etc). Formulated as complete meals (NOT supplementation)

Mediums:
- 400-450gram re-sealable doy packs
- 400-450gram re-sealable tin cans

Look n Feel:
Korunui - https://korunuipantry.com
Mela Vo - https://www.melvo.example.nz/
Lantern ridge - https://dinebrightstaybright.example.nz/collections/cereals

The name of our products may/may not be “tuatara bowl”. Our on-going research tells us that for the Asian market, an icon or character to personify our product may be a sound strategy. This is only for the designer to take note off.

Deliverables:
* 5 packaging designs in the range.
1x yellow + orange colored foods (star ingredient: “sun kept” – passion fruit powder)
1x red colored foods (star ingredient: (star ingredient: - Manuka honey )
1x blues/purple colored foods: (star ingredient: nolari blackcurrant)
1 x green coloured foods (star ingredient: Green kiwi)
1 x brown/white (star ingredients: brandon’s grass fed bone broth)

brand name, please use “TuataraBowl” for now.

These will be the products:

Blue/purple: “Instant oatmeal porridge”
Ingredients: Rolled Baby Oats, Blueberries, Blackcurrant Powder, chia seeds, Blue Spirulina, Sheep’s Milk.
Star ingredient: Blackcurrant powder (support eyesight)

Brown/White: “Instant Brown Rice”
Ingredients: Organic Brown Rice, Grass fed bone broth powder, collagen peptide powder, black sesame seeds, onions and garlic powder, dried mushrooms, probiotics.
Star ingredient: Grass fed bone broth (support joint health)

Green: “Instant Smoothie”
Ingredients: Organic Green Kiwifruit, Kale powder, green apple powder, whey protein concentrate, probiotics, and sheep’s milk powder
Star ingredient: Organic green kiwi fruit(supports immunity)

Yellow/Orange “Instant Oatmeal”
Ingredients: Organic rolled baby oats, banana, organic passionfruit, apricot, dried mango, probiotics, cinnamon, sheep’s milk powder.
Star ingredient: Organic passionfruit(regulates blood glucose)

Red: “ instant amaranth cereal”
Ingredients: Organic amaranth, red apples, pomegranate, cranberries, Manuka honey powder, probiotics, sheep’s milk
Star ingredient: Manuka honey powder (anti-inflammatory)

Target Market(s)

Whose attention we are trying to grab?

Primary:
- 20 to 40 year olds buying these products for their parents/grand parents
- Health Nutrition conscious “golden agers”
Secondary
- Professional Caregivers to the elderly (homes, private hospitals etc)
- 40 year olds in the “prevention” mind set.

Font styles to use
Serif
Sans Serif

Colors

Designer to choose colors to be used in the design.

Requirements
Must have
• Mandatory:
• - clear visual que of the food color/s
• - "New Zealand" origin must come through strongly.
• - must have a blurp or feature of the star ingredient for each with mention of brand.
• e.g. for the blues+ purple, NZ blackcurrant powder for improved eyesight (cataract prevention).
• - icons for “heart health, “eyesight”, “mobility”, “gut-health”.
• - every other ingredient must be stated.
• The name of product may/may not be “tuatarabowl”. Our on-going research tells us that for the Asian market, an icon or character to personify our product may be a sound strategy. This is only for the designer to take note off.
Nice to have
• Desirables:
• Ingredient origin story - e.g blackcurrant comes from Timaru etc.
• (refer to Pembertons destination marketing…)

```html
<!DOCTYPE html>
<html lang="en">
<head>
<meta charset="utf-8">
<title>TuataraBowl Instant Oatmeal – Pouch Front</title>
<link rel="stylesheet" href="https://fonts.googleapis.com/css2?family=Ubuntu:wght@400;500;700&display=swap">
<style>
  :root {
    --backdrop: #f1f1f1;
    --pouch: #ffffff;
    --ink: #2a2a2a;
    --orange: #e0601a;
    --orange-soft: #ec8a4c;
    --icon-grey: #8c8c8c;
    --label-grey: #9a9a9a;
    --oat-light: #efe9e1;
    --oat-mid: #d9ccbc;
  }
  * { box-sizing: border-box; margin: 0; padding: 0; }
  html, body {
    width: 1200px; height: 1200px; overflow: hidden;
    background: var(--backdrop);
    font-family: "Ubuntu", sans-serif;
  }
  .pouch-front {
    position: absolute; left: 290px; top: 60px;
    width: 620px; height: 1080px;
    background: var(--pouch);
    border-radius: 22px;
    box-shadow: 0 10px 40px rgba(0,0,0,0.08);
  }
  .brand-name {
    position: absolute; top: 255px; left: 0; width: 100%;
    text-align: center; font-weight: 700; font-size: 56px;
    color: var(--ink); letter-spacing: -1px;
  }
  .rule {
    position: absolute; left: 130px; width: 360px; height: 1.5px;
    background: linear-gradient(90deg, transparent, var(--orange) 15%, var(--orange) 85%, transparent);
  }
  .rule--top { top: 365px; }
  .rule--under-title { top: 454px; }
  .rule--icons-top { top: 904px; left: 110px; width: 400px; }
  .rule--icons-bottom { top: 997px; left: 110px; width: 400px; }
  .product-title {
    position: absolute; top: 372px; width: 100%; text-align: center;
    font-weight: 500; font-size: 58px; color: var(--orange);
  }
  .made-with {
    position: absolute; top: 472px; width: 100%; text-align: center;
    font-size: 17px; color: var(--orange);
  }
  .star-ingredient {
    position: absolute; top: 493px; width: 100%; text-align: center;
    font-weight: 500; font-size: 30px; color: var(--orange);
  }
  .benefit-pill {
    position: absolute; top: 536px; left: 50%; transform: translateX(-50%);
    padding: 2px 10px; border-radius: 8px;
    background: var(--orange); color: #fff; font-size: 17px; white-space: nowrap;
  }
  .hero-visual {
    position: absolute; top: 608px; left: 190px;
    width: 274px; height: 274px; border-radius: 50%;
    background: radial-gradient(circle at 45% 45%, var(--oat-light), var(--oat-mid));
    box-shadow: 0 0 0 6px #f4f4f4, 0 8px 18px rgba(0,0,0,0.12);
  }
  .benefit-icons {
    position: absolute; top: 918px; left: 0; width: 100%; height: 70px;
  }
  .benefit {
    position: absolute; top: 0; width: 100px; margin-left: -50px;
    text-align: center; color: var(--label-grey); font-size: 12px;
  }
  .benefit svg { display: block; margin: 0 auto 6px; height: 46px; }
  .net-weight {
    position: absolute; top: 1016px; width: 100%; text-align: center;
    font-size: 20px; color: var(--orange-soft);
  }
</style>
</head>
<body>
  <main class="pouch-front">
    <div class="brand-name">TuataraBowl</div>
    <div class="rule rule--top"></div>
    <h1 class="product-title">Instant Oatmeal</h1>
    <div class="rule rule--under-title"></div>
    <p class="made-with">Made With</p>
    <p class="star-ingredient">Organic Passion Fruit</p>
    <span class="benefit-pill">Regulates Blood Glucose</span>

    <div class="hero-visual" role="img" aria-label="Bowl of creamy oatmeal with halved passion fruit beside it"></div>

    <div class="rule rule--icons-top"></div>
    <section class="benefit-icons">
      <div class="benefit" style="left:163px">
        <svg viewBox="0 0 48 46" width="48" aria-hidden="true"><path fill="var(--icon-grey)" d="M24 44 C8 32 2 24 2 14 A11 11 0 0 1 24 9 A11 11 0 0 1 46 14 C46 24 40 32 24 44Z"/></svg>
        Heart Health
      </div>
      <div class="benefit" style="left:259px">
        <svg viewBox="0 0 80 46" width="80" aria-hidden="true"><path fill="none" stroke="var(--icon-grey)" stroke-width="5" d="M4 23 Q40 -6 76 23 Q40 52 4 23Z"/><circle cx="40" cy="23" r="11" fill="none" stroke="var(--icon-grey)" stroke-width="5"/><circle cx="40" cy="23" r="5" fill="var(--icon-grey)"/></svg>
        Eyesight
      </div>
      <div class="benefit" style="left:345px">
        <svg viewBox="0 0 46 46" width="46" aria-hidden="true"><g fill="none" stroke="var(--icon-grey)" stroke-width="5" stroke-linecap="round"><path d="M24 12 L18 26 L26 32 L24 44"/><path d="M18 26 L8 44"/><path d="M10 18 L22 12 L30 20 L38 18"/></g><circle cx="32" cy="6" r="5" fill="var(--icon-grey)"/></svg>
        Mobility
      </div>
      <div class="benefit" style="left:438px">
        <svg viewBox="0 0 40 46" width="40" aria-hidden="true"><path fill="none" stroke="var(--icon-grey)" stroke-width="2.5" d="M14 2 V12 Q14 16 20 16 H26 Q36 16 36 28 Q36 40 24 40 Q16 40 14 34 Q12 30 8 32 L4 36 V44"/><path fill="none" stroke="var(--icon-grey)" stroke-width="2.5" d="M22 2 V8 Q22 10 26 10 Q30 10 30 14"/></svg>
        Gut-Health
      </div>
    </section>
    <div class="rule rule--icons-bottom"></div>

    <p class="net-weight">Net weight: 450g</p>
  </main>
</body>
</html>
```